One page design needed for a veteran owned brewery

I need a one page web designed for a brewery that is veteran owned. We give back a portion of our proceeds to veteran based nonprofit groups. halvardbrewing.example It is word press based.

Industry/Entity Type

Craft Brewery

Number of Pages Required

1 page

```html
<!DOCTYPE html>
<html lang="en">
<head>
<meta charset="utf-8">
<title>Halvard Brewery</title>
<link href="https://fonts.googleapis.com/css2?family=Raleway:wght@400;500;600;700&family=Montserrat:wght@600;700&family=Open+Sans:wght@400;600&display=swap" rel="stylesheet">
<style>
:root{
  --green:#6b9a2d;
  --green-dark:#5a8424;
  --cream:#f4ecd8;
  --cream-deep:#eadfc4;
  --ink:#333;
  --muted:#666;
  --dark:#1e1e1e;
  --footer:#222;
  --white:#fff;
  --star:#e9a825;
}
*{box-sizing:border-box;margin:0;padding:0}
html,body{width:1200px;height:3774px;overflow:hidden}
body{position:relative;font-family:"Open Sans",sans-serif;color:var(--ink);background:var(--cream)}
.abs{position:absolute}

/* header */
.site-header{left:0;top:0;width:1200px;height:113px;background:var(--white);border-top:4px solid var(--green);z-index:5}
.brand-badge{left:125px;top:18px;width:165px;height:165px;border-radius:50%;background:var(--white);display:flex;align-items:center;justify-content:center;text-align:center;z-index:6;box-shadow:0 2px 6px rgba(0,0,0,.15)}
.brand-name{font-family:"Montserrat",sans-serif;font-weight:700;color:#2a2a2a;line-height:1.15;font-size:20px}
.main-nav{top:46px;left:540px;display:flex;gap:0;font-family:"Raleway",sans-serif;font-weight:600;font-size:13px;color:#333}
.main-nav a{position:absolute;white-space:nowrap;text-decoration:none;color:#333}
.main-nav a.active{color:var(--green)}
.search-btn{left:1038px;top:32px;width:48px;height:48px;border:2px solid var(--green);border-radius:50%}

/* hero */
.hero{left:0;top:113px;width:1200px;height:596px;background:linear-gradient(180deg,#3f4f78 0%,#6b3d3a 28%,#4a2e1f 45%,#3a2416 75%,#2a1a10 100%)}
.hero-title{left:0;top:490px;width:1200px;text-align:center;font-family:"Montserrat",sans-serif;font-weight:700;font-size:44px;color:var(--white);letter-spacing:1px}
.hero-sub{left:0;top:556px;width:1200px;text-align:center;font-family:"Montserrat",sans-serif;font-weight:600;font-size:13.5px;line-height:30px;color:var(--white);text-transform:uppercase}

/* section headings */
.section-title{font-family:"Raleway",sans-serif;font-weight:500;font-size:46px;color:#333;text-transform:uppercase;letter-spacing:.5px}
.section-title span{color:var(--green)}
.title-rule{height:4px;width:78px;background:var(--green)}
.body-text{font-size:11.5px;line-height:26px;color:#444}
.btn-outline{border:2px solid var(--green);color:var(--green);font-family:"Raleway",sans-serif;font-weight:600;font-size:14px;display:flex;align-items:center;justify-content:center;background:transparent}
.btn-solid{background:var(--green);color:var(--white);font-family:"Raleway",sans-serif;font-weight:700;font-size:14px;display:flex;align-items:center;justify-content:center;gap:8px}

/* about */
.about{left:0;top:709px;width:1200px;height:561px;background:radial-gradient(ellipse at 50% 40%,#f8f2e3,var(--cream) 70%,var(--cream-deep))}
.about-brand{left:660px;top:805px;width:385px;height:345px;display:flex;align-items:center;justify-content:center;gap:16px}
.about-brand .dot{width:44px;height:44px;border-radius:50%;background:var(--green)}
.about-brand .brand-name{font-size:46px;color:#3a2a1a}

/* products */
.products-rule{left:0;top:1268px;width:1200px;height:4px;background:var(--green)}
.products-tab{left:455px;top:1268px;width:290px;height:54px;background:var(--green);border-radius:0 0 40px 40px;color:var(--white);font-family:"Raleway",sans-serif;font-weight:500;font-size:28px;display:flex;align-items:center;justify-content:center}
.product-card{top:1386px;height:395px;background:var(--white);border:1px solid #e2dccd;box-shadow:0 1px 3px rgba(0,0,0,.08);text-align:center}
.product-photo{position:absolute;left:12px;top:12px;right:12px;height:250px}
.stars{position:absolute;left:0;right:0;top:282px;font-size:14px;color:var(--star);letter-spacing:2px}
.stars i{font-style:normal;color:#999}
.product-name{position:absolute;left:0;right:0;top:306px;font-family:"Montserrat",sans-serif;font-weight:600;font-size:17px;color:#333}
.product-desc{position:absolute;left:0;right:0;top:336px;font-size:11.5px;color:#555}
.pager-dot{top:1808px;width:16px;height:16px;border-radius:50%;border:2px solid var(--green)}

/* manufacture */
.manufacture{left:0;top:1877px;width:1200px;height:491px;background:linear-gradient(90deg,#232323,#2c2c2c 55%,#1a1a1a)}
.manufacture .section-title{color:var(--white)}
.manufacture .body-text{color:#e8e8e8}
.manufacture-photo{left:705px;top:1877px;width:495px;height:491px;background:radial-gradient(ellipse at 55% 45%,#c88a2c 0%,#8a5a1c 35%,#3a3530 70%,#2a2a2a 100%)}

/* testimonials */
.testimonials{left:0;top:2368px;width:1200px;height:1056px;background:radial-gradient(ellipse at 50% 30%,#f8f2e3,var(--cream) 65%,var(--cream-deep))}
.quote-card{top:2511px;height:220px;background:var(--white);border:1px solid #ddd4c0;padding:22px 20px}
.quote-card::after{content:"";position:absolute;left:40px;bottom:-10px;width:18px;height:18px;background:var(--white);border-right:1px solid #ddd4c0;border-bottom:1px solid #ddd4c0;transform:rotate(45deg)}
.quote-head{font-size:16px;color:var(--star);letter-spacing:2px}
.quote-head b{color:#888;font-family:Georgia,serif;font-size:24px;margin-right:8px;letter-spacing:0}
.quote-text{margin-top:8px;font-size:11px;line-height:20.5px;color:#666}
.avatar{top:2762px;width:64px;height:64px;border-radius:50%;background:linear-gradient(135deg,#b48a6c,#6a4a38)}
.author{top:2771px;font-family:"Montserrat",sans-serif;font-weight:600;font-size:14px;color:#333}
.author small{display:block;font-family:"Open Sans",sans-serif;font-weight:400;font-size:11px;color:#666;margin-top:4px}
.divider{left:111px;top:2873px;width:978px;height:1px;background:#d8ceb6}

/* contact */
.field{left:143px;width:426px;background:var(--white);border:1px solid #e0d8c5;font-family:"Raleway",sans-serif;font-weight:600;font-size:12px;color:#333;padding:16px 14px}
.contact-photo{left:717px;top:2931px;width:302px;height:440px;background:linear-gradient(90deg,rgba(0,0,0,0) 0%,#e8a036 18%,#c97a1c 42%,#8a2418 58%,#6a1c12 82%,rgba(0,0,0,0) 100%);border-radius:30px 30px 20px 20px}

/* footer */
.site-footer{left:0;top:3424px;width:1200px;height:350px;background:var(--footer)}
.footer-brand{left:520px;top:3442px;width:160px;height:160px;border-radius:50%;background:var(--white);display:flex;align-items:center;justify-content:center;text-align:center}
.footer-rule{left:111px;top:3613px;width:978px;height:1px;background:#3a3a3a}
.social{top:3633px;width:60px;height:60px;border-radius:50%;border:1px solid #777;display:flex;align-items:center;justify-content:center}
.copyright{left:0;top:3726px;width:1200px;text-align:center;font-size:11.5px;color:#ddd}
</style>
</head>
<body>

<header class="abs site-header">
  <nav class="abs main-nav" aria-label="Main">
    <a class="active" style="left:0">HOME</a>
    <a style="left:97px">ABOUT</a>
    <a style="left:188px">PRODUCT</a>
    <a style="left:297px">TESTIMONIAL</a>
    <a style="left:428px">CONTACT</a>
  </nav>
  <div class="abs search-btn">
    <svg width="44" height="44" viewBox="0 0 44 44"><circle cx="21" cy="21" r="5" fill="none" stroke="#6b9a2d" stroke-width="2"/><line x1="25" y1="25" x2="28" y2="28" stroke="#6b9a2d" stroke-width="2"/></svg>
  </div>
</header>
<div class="abs brand-badge"><div class="brand-name">HALVARD<br>BREWERY</div></div>

<section class="abs hero" role="img" aria-label="Waving American flag over a dark wooden tabletop"></section>
<h1 class="abs hero-title">HALVARD BREWERY</h1>
<p class="abs hero-sub">We are a veteran owned &amp; operated brewery. Our goal is to donate a percentage of<br>our proceeds to veteran organizations and our local heroes.</p>

<section class="abs about"></section>
<h2 class="abs section-title" style="left:111px;top:770px">About <span>Us</span></h2>
<div class="abs title-rule" style="left:111px;top:836px"></div>
<p class="abs body-text" style="left:111px;top:866px;width:480px">Halvard Brewery is a craft brewery in Halvard, IN that will have a wide breadth of beers with a full kitchen.We believe the transition from military life to civilian life can be a difficult road. We are trained by the military to be tough, battle harden soldiers ready for transition from military combat.</p>
<p class="abs body-text" style="left:111px;top:996px;width:480px">However, the exit training is not nearly enough to fight the difference of civilian life leaving some vets feeling left behind and causing many to take their own life. The Halvard Brew- ery team will work to change that! We believe the transition from military life to civilian life can be a difficult road.</p>
<div class="abs btn-outline" style="left:111px;top:1136px;width:132px;height:46px">READ MORE</div>
<div class="abs about-brand"><span class="dot"></span><span class="brand-name">HALVARD</span></div>

<div class="abs products-rule"></div>
<div class="abs products-tab">OUR PRODUCTS</div>

<article class="abs product-card" style="left:111px;width:234px">
  <div class="product-photo" role="img" aria-label="Amber and green beer bottles" style="background:linear-gradient(90deg,#fff 10%,#b0501a 30%,#d07a2a 45%,#2e7a2a 60%,#1f5a1f 78%,#fff 92%)"></div>
  <div class="stars">★★★★<i>☆</i></div><h3 class="product-name">PRODUCT NAME</h3><p class="product-desc">Sed ut perspiciatis unde omnis iste</p>
</article>
<article class="abs product-card" style="left:360px;width:231px">
  <div class="product-photo" role="img" aria-label="Two golden beer bottles" style="background:linear-gradient(90deg,#fff 10%,#e0b040 30%,#f0cc6a 50%,#d8a83a 70%,#fff 90%)"></div>
  <div class="stars">★★★★<i>☆</i></div><h3 class="product-name">PRODUCT NAME</h3><p class="product-desc">Sed ut perspiciatis unde omnis iste</p>
</article>
<article class="abs product-card" style="left:606px;width:232px">
  <div class="product-photo" role="img" aria-label="Single brown beer bottle" style="background:linear-gradient(90deg,#fff 30%,#8a3a14 45%,#b05a22 55%,#fff 70%)"></div>
  <div class="stars">★★★★<i>☆</i></div><h3 class="product-name">PRODUCT NAME</h3><p class="product-desc">Sed ut perspiciatis unde omnis iste</p>
</article>
<article class="abs product-card" style="left:853px;width:234px">
  <div class="product-photo" role="img" aria-label="Golden, green and brown beer bottles" style="background:linear-gradient(90deg,#fff 8%,#d8aa40 25%,#2e7a2a 50%,#5a3018 75%,#fff 92%)"></div>
  <div class="stars">★★★★<i>☆</i></div><h3 class="product-name">PRODUCT NAME</h3><p class="product-desc">Sed ut perspiciatis unde omnis iste</p>
</article>
<div class="abs pager-dot" style="left:571px"></div>
<div class="abs pager-dot" style="left:592px;background:var(--green)"></div>
<div class="abs pager-dot" style="left:613px"></div>

<section class="abs manufacture"></section>
<div class="abs manufacture-photo" role="img" aria-label="Two beer bottles resting on ice cubes"></div>
<h2 class="abs section-title" style="left:109px;top:1928px;color:#fff">Manufacture <span>Beer</span></h2>
<p class="abs body-text" style="left:111px;top:2010px;width:490px;color:#e8e8e8">Sed ut perspiciatis unde omnis iste natus error sit voluptatem accusantium doloremque lau dan tium, totam rem aperiam, eaque ipsa quae ab illo inventore veritatis et quasi archite cto beatae vitae dicta sunt explicabo. Nemo enim ipsam voluptatem quia voluptas sit asper natur aut odit aut fugit, sed quia consequuntur magni dolores eos qui ratione voluptatem sequi eaque ipsa quae ab illo inventore nesciunt.</p>
<p class="abs body-text" style="left:111px;top:2156px;width:490px;color:#e8e8e8">Nemo enim ipsam voluptatem quia voluptas sit asper natur aut odit aut fugit, sed quia conse quuntur magni dolores eos qui ratione voluptatem sequi nesciunt eaque ipsa quae ab illo inventore quia voluptas sit asper nesciunt.</p>
<div class="abs btn-solid" style="left:111px;top:2266px;width:132px;height:46px">READ MORE</div>

<section class="abs testimonials"></section>
<h2 class="abs section-title" style="left:0;top:2412px;width:1200px;text-align:center">Our <span>Testimonials</span></h2>
<div class="abs title-rule" style="left:561px;top:2476px"></div>

<article class="abs quote-card" style="left:111px;width:317px"><div class="quote-head"><b>“</b>★★★★★</div><p class="quote-text">Sed ut perspiciatis unde omnis iste natus error sit voluptatem accusantium doloremque laudantium, totam rem aperiam, eaque ipsa quae ab illo inven tore veritatis et quasi architecto beatae vitae dicta sunt explicabo. Nemo enim ipsam voluptatem quia tatem sequi nesciunt.</p></article>
<article class="abs quote-card" style="left:443px;width:314px"><div class="quote-head"><b>“</b>★★★★★</div><p class="quote-text">Sed ut perspiciatis unde omnis iste natus error sit voluptatem accusantium doloremque laudantium, totam rem aperiam, eaque ipsa quae ab illo inven tore veritatis et quasi architecto beatae vitae dicta sunt explicabo. Nemo enim ipsam voluptatem quia tatem sequi nesciunt.</p></article>
<article class="abs quote-card" style="left:772px;width:317px"><div class="quote-head"><b>“</b>★★★★★</div><p class="quote-text">Sed ut perspiciatis unde omnis iste natus error sit voluptatem accusantium doloremque laudantium, totam rem aperiam, eaque ipsa quae ab illo inven tore veritatis et quasi architecto beatae vitae dicta sunt explicabo. Nemo enim ipsam voluptatem quia tatem sequi nesciunt.</p></article>

<div class="abs avatar" style="left:124px" role="img" aria-label="Customer portrait"></div>
<div class="abs author" style="left:204px">Jhon Smith<small>Posted on 16 Jan 2019</small></div>
<div class="abs avatar" style="left:455px" role="img" aria-label="Customer portrait"></div>
<div class="abs author" style="left:535px">Jhon Smith<small>Posted on 16 Jan 2019</small></div>
<div class="abs avatar" style="left:785px" role="img" aria-label="Customer portrait"></div>
<div class="abs author" style="left:865px">Jhon Smith<small>Posted on 16 Jan 2019</small></div>

<div class="abs divider"></div>

<h2 class="abs section-title" style="left:143px;top:2920px">Contact <span>Us</span></h2>
<div class="abs field" style="top:3014px;height:50px">Name:</div>
<div class="abs field" style="top:3070px;height:50px">Email:</div>
<div class="abs field" style="top:3127px;height:50px">Phone:</div>
<div class="abs field" style="top:3185px;height:112px">Message:</div>
<div class="abs btn-solid" style="left:423px;top:3271px;width:118px;height:40px">SUBMIT
  <svg width="16" height="16" viewBox="0 0 16 16"><circle cx="8" cy="8" r="6.5" fill="none" stroke="#fff" stroke-width="1.5"/><path d="M6 5l3 3-3 3" fill="none" stroke="#fff" stroke-width="1.5"/></svg>
</div>
<div class="abs contact-photo" role="img" aria-label="Two pint glasses of lager and red ale with foam"></div>

<footer class="abs site-footer"></footer>
<div class="abs footer-brand"><div class="brand-name" style="font-size:19px">HALVARD<br>BREWERY</div></div>
<div class="abs footer-rule"></div>
<div class="abs social" style="left:388px" aria-label="Social link"></div>
<div class="abs social" style="left:458px" aria-label="Social link"></div>
<div class="abs social" style="left:529px" aria-label="Social link"></div>
<div class="abs social" style="left:602px" aria-label="Social link"></div>
<div class="abs social" style="left:672px" aria-label="Social link"></div>
<div class="abs social" style="left:745px" aria-label="Email">
  <svg width="18" height="14" viewBox="0 0 18 14"><rect x="1" y="1" width="16" height="12" fill="none" stroke="#fff" stroke-width="1.4"/><path d="M1 1l8 7 8-7" fill="none" stroke="#fff" stroke-width="1.4"/></svg>
</div>
<p class="abs copyright">© Copyrights 2019 - Halvard Brewery All Rights Reserved.</p>

</body>
</html>
```